Runlark

I have a web site RUNLARK.com that is in serious need of a re-design. The site is mean't to be a portal for an app that I have called RUNLARK which you can see in the App Market or googleplay. Take a look and see what you can do.
Updates

Project Deadline Extended
Reason: Still working with designers. The "look" is not quite there but a lot of progress has been made. MB

Industry/Entity Type

Store

```html
<!DOCTYPE html>
<html lang="en">
<head>
<meta charset="utf-8">
<title>Runlark — Sports Portal</title>
<link href="https://fonts.googleapis.com/css2?family=Roboto+Condensed:wght@400;700&family=Open+Sans:ital,wght@0,400;0,600;1,400;1,600&display=swap" rel="stylesheet">
<style>
:root{
  --black:#111214;
  --ink:#2a2a2a;
  --muted:#555;
  --blue:#1f74c9;
  --navy:#0f3d8a;
  --logo:#1a4a9c;
  --panel:#ebebeb;
  --light:#f3f3f3;
  --white:#fff;
}
*{box-sizing:border-box;margin:0;padding:0}
html,body{width:867px;height:1200px;overflow:hidden}
body{position:relative;font-family:"Open Sans",sans-serif;color:var(--ink);background:var(--white)}
.abs{position:absolute}
.cond{font-family:"Roboto Condensed",sans-serif}

.topbar{left:0;top:0;width:867px;height:35px;background:var(--black)}
.social{left:80px;top:7px;display:flex;gap:4px}
.social span{width:20px;height:20px;background:#3a3a3a;display:block}
.social span:first-child{background:#3b5fb0}
.toplinks{right:82px;top:10px;font-size:10px;color:#888}
.toplinks b{color:#fff;font-weight:600}

.header{left:0;top:35px;width:867px;height:69px;background:var(--white)}
.logo{left:80px;top:15px;display:flex;align-items:center;gap:8px;font-family:"Roboto Condensed",sans-serif;font-size:32px;font-weight:700;color:var(--logo)}
.logo i{width:22px;height:22px;border-radius:50%;background:#2e9a3c;display:block}
.nav{left:349px;top:27px;display:flex;gap:30px;font-size:13.5px;color:#222}
.nav .on{color:var(--navy)}

.hero{left:0;top:104px;width:867px;height:430px;background:linear-gradient(90deg,#1b1a1a,#3a2e28 30%,#2a2422 70%,#161616)}
.slide{left:81px;top:122px;width:705px;height:309px;border:2px solid #111;background:radial-gradient(circle at 60% 40%,#a06a3c,#3c2a20 55%,#1c1612)}
.caption{left:83px;top:375px;width:701px;height:54px;background:rgba(0,0,0,.7);color:#fff;padding:8px 12px}
.caption h2{font-family:"Open Sans",sans-serif;font-weight:400;font-size:15px}
.caption p{font-size:9.5px;font-weight:600;margin-top:4px}
.arrowbtn{width:33px;height:33px}

.tabs{left:147px;top:446px;width:573px;height:72px;display:flex;background:#fff;border:1px solid #ddd}
.tab{width:191px;height:70px;position:relative;padding:10px 0 0 13px;border-right:1px solid #ddd}
.tab h3{font-family:"Roboto Condensed",sans-serif;font-weight:400;font-size:17px;color:#222}
.tab p{font-size:9.5px;line-height:14px;margin-top:5px;color:#333}
.tab .ph{position:absolute;right:2px;top:2px;width:70px;height:66px}
.tab.on{background:var(--blue)}
.tab.on h3,.tab.on p{color:#fff}

.stage{left:0;top:533px;width:867px;height:262px;background:linear-gradient(180deg,#3a3430,#1e1a18 60%,#0e0e0e)}
.board{left:81px;top:555px;width:705px;height:219px;background:linear-gradient(180deg,#f2f2f2,#bdbdbd)}
.card{top:572px;width:197px;height:183px;background:#fff;border:2px solid #fff;box-shadow:0 0 2px rgba(0,0,0,.3)}
.card h4{font-family:"Roboto Condensed",sans-serif;font-weight:400;font-size:14.5px;color:var(--navy);padding:7px 0 0 11px;height:31px;position:relative;white-space:nowrap}
.card h4 em{position:absolute;right:10px;top:11px;font-style:normal;letter-spacing:2px;color:var(--navy);font-size:7px;line-height:8px}
.card .pic{width:193px;height:148px}
.pitch{background:linear-gradient(180deg,#1f2a22,#3d6a2c 45%,#4a7d30)}
.score{color:#fff;text-align:center}

.content{left:0;top:795px;width:867px;height:271px;background:var(--light)}
.tabhead{height:31px;font-family:"Roboto Condensed",sans-serif;font-size:15.5px;display:flex;align-items:center;padding-left:14px}
.item{position:absolute;width:213px;height:60px;background:#e9e9e9}
.item .th{position:absolute;left:7px;top:5px;width:51px;height:49px;background:linear-gradient(135deg,#6a4a36,#2b2622)}
.item h5{position:absolute;left:64px;top:5px;font-style:italic;font-weight:400;font-size:11.5px;color:#222}
.item p{position:absolute;left:64px;top:24px;font-size:9.5px;line-height:13px;color:#444;width:145px}
.item.alt{background:#dedede}
.item.blue h5{color:var(--navy)}

.mid h3{font-family:"Roboto Condensed",sans-serif;font-weight:400;font-size:15.5px;color:var(--navy)}
.mid p{font-size:10.5px;line-height:15.5px;color:#444;text-align:justify;margin-top:10px;width:213px}
.sponsors{left:327px;top:968px;width:213px;height:75px;background:#e6e6e6;padding:6px 13px}
.sponsors .dots{position:absolute;right:12px;top:12px;letter-spacing:2px;color:var(--navy);font-size:7px;line-height:8px}
.badges{position:absolute;left:8px;top:36px;display:flex;gap:7px}
.badges span{width:35px;height:35px;border-radius:50%;display:block}

.footer{left:0;top:1066px;width:867px;height:98px;background:var(--black);color:#fff}
.footer h3{font-family:"Roboto Condensed",sans-serif;font-size:15px;font-weight:400;position:absolute}
.store{top:38px;width:133px;height:39px;border:2px solid #fff;border-radius:4px;padding:4px 0 0 40px;font-size:8px;line-height:10px;white-space:nowrap;overflow:hidden}
.store b{display:block;font-weight:400;font-size:15px;line-height:18px;letter-spacing:-.2px}
.store i{position:absolute;left:10px;top:7px;width:22px;height:22px;background:#fff;border-radius:3px}
.email{left:518px;top:43px;width:239px;height:28px;background:#2a2a2a;font-size:9px;font-style:italic;color:#888;padding:8px 0 0 46px}
.send{left:757px;top:43px;width:29px;height:28px;background:var(--blue)}

.bottombar{left:0;top:1164px;width:867px;height:36px;background:#f0f0f0;font-size:9.5px;color:#444}
.bottombar .links{position:absolute;left:80px;top:12px}
.bottombar .links a{color:var(--navy);text-decoration:none}
.bottombar .copy{position:absolute;right:81px;top:12px}
</style>
</head>
<body>

<div class="abs topbar">
  <div class="abs social"><span></span><span></span><span></span><span></span><span></span><span></span><span></span></div>
  <div class="abs toplinks"><b>FAQ</b> &nbsp;/&nbsp; CONTACT US</div>
</div>

<header class="abs header">
  <div class="abs logo"><i></i>Runlark</div>
  <nav class="abs nav cond"><span class="on">HOME</span><span>ABOUT US</span><span>EVENTS</span><span>PHOTOS</span><span>LIVE SCORE</span><span>SPORTS NEWS</span></nav>
</header>

<section class="abs hero"></section>
<div class="abs slide" role="img" aria-label="Basketball players leaping for the ball in front of a crowd"></div>
<div class="abs caption">
  <h2>Lorem ipsum dolor sit amet consectetur adipiscing elit</h2>
  <p>Proin ornare augue purus, eu cursus nibh vestibulum quis. Sed id nisi eget odio consectetur imperdiet.</p>
</div>
<svg class="abs arrowbtn" style="left:33px;top:264px" viewBox="0 0 33 33"><circle cx="16.5" cy="16.5" r="15" fill="none" stroke="#fff" stroke-width="2"/><path d="M19 9l-7 7.5 7 7.5" fill="none" stroke="#fff" stroke-width="2.5"/></svg>
<svg class="abs arrowbtn" style="left:801px;top:260px" viewBox="0 0 33 33"><circle cx="16.5" cy="16.5" r="15" fill="none" stroke="#777" stroke-width="2"/><path d="M14 9l7 7.5-7 7.5" fill="none" stroke="#777" stroke-width="2.5"/></svg>

<div class="abs tabs">
  <div class="tab on"><h3>Basketball</h3><p>Lorem ipsum dolor<br>sit amet, consectetur</p><div class="ph" role="img" aria-label="Basketball player with ball" style="background:linear-gradient(135deg,#c9783a,#2a2a3a)"></div></div>
  <div class="tab"><h3>Hockey</h3><p>Lorem ipsum dolor<br>sit amet, consectetur</p><div class="ph" role="img" aria-label="Hockey goalie in red kit" style="background:linear-gradient(135deg,#c8343a,#e8e8ec)"></div></div>
  <div class="tab" style="border-right:0"><h3>Baseball</h3><p>Lorem ipsum dolor<br>sit amet, consectetur</p><div class="ph" role="img" aria-label="Baseball pitcher on the field" style="background:linear-gradient(180deg,#3a4a3a,#4f8a3a)"></div></div>
</div>

<section class="abs stage" role="img" aria-label="Crowd of athletes in action"></section>
<div class="abs board"></div>
<svg class="abs" style="left:91px;top:653px" width="14" height="22" viewBox="0 0 14 22"><path d="M11 2L3 11l8 9" fill="none" stroke="#2a6fc0" stroke-width="3"/></svg>
<svg class="abs" style="left:762px;top:653px" width="14" height="22" viewBox="0 0 14 22"><path d="M3 2l8 9-8 9" fill="none" stroke="#111" stroke-width="3"/></svg>

<div class="abs card" style="left:116px">
  <h4>RECENT RESULTS<em>●●●●●●●</em></h4>
  <div class="pic pitch" role="img" aria-label="Football pitch under stadium lights" style="position:relative">
    <div class="score abs" style="left:0;width:193px;top:24px;font-size:15px">Prima League</div>
    <svg class="abs" style="left:17px;top:63px" width="38" height="46" viewBox="0 0 38 46"><path d="M2 2h34v22c0 10-8 17-17 20C10 41 2 34 2 24z" fill="#c8202e" stroke="#e8c84a" stroke-width="2"/></svg>
    <svg class="abs" style="left:142px;top:60px" width="38" height="48" viewBox="0 0 38 48"><path d="M2 2h34v24c0 10-8 17-17 20C10 43 2 36 2 26z" fill="#e8e8e8" stroke="#1a3a8a" stroke-width="2"/></svg>
    <div class="score abs" style="left:0;width:193px;top:68px;font-size:33px;font-family:'Open Sans',sans-serif">2 - 2</div>
    <div class="score abs" style="left:0;width:193px;top:112px;font-size:9px">02 Jan 2013</div>
    <div class="score abs" style="left:24px;top:134px;font-size:10px;font-weight:600">Milford</div>
    <div class="score abs" style="left:148px;top:134px;font-size:10px;font-weight:600">Norvale</div>
  </div>
</div>
<div class="abs card" style="left:335px">
  <h4>PLAYERS<em>●●●●●●●</em></h4>
  <div class="pic" role="img" aria-label="Footballer in a striped kit raising his arm" style="position:relative;background:linear-gradient(160deg,#4a4a4a,#2c2c40 50%,#7a2040)">
    <div class="abs" style="left:0;bottom:0;width:193px;height:26px;background:rgba(0,0,0,.55);color:#fff;font-size:10.5px;padding:6px 10px;white-space:nowrap"><i style="font-weight:600">Leo Varga Football</i> &nbsp; <span style="color:#aaa;font-size:9.5px">Valdoria</span></div>
  </div>
</div>
<div class="abs card" style="left:554px">
  <h4>SCHEDULES<em>●●●●●●●</em></h4>
  <div class="pic pitch" role="img" aria-label="Empty floodlit football stadium"></div>
</div>

<section class="abs content"></section>

<div class="abs" style="left:80px;top:820px;width:213px;display:flex">
  <div class="tabhead" style="width:114px;background:#e3e3e3;color:var(--navy)">POPULAR</div>
  <div class="tabhead" style="width:99px;background:var(--navy);color:#fff;padding-left:25px">LATEST</div>
</div>
<div class="item blue" style="left:80px;top:853px;background:#f0f0f0"><div class="th" role="img" aria-label="Athlete portrait"></div><h5>Lorem ipsum dolor sit .</h5><p>Proin ornare augue purus, eu cursus nibh vestibulum quis.</p></div>
<div class="item alt" style="left:80px;top:918px"><div class="th" role="img" aria-label="Athlete portrait"></div><h5>Lorem ipsum dolor sit .</h5><p>Proin ornare augue purus, eu cursus nibh vestibulum quis.</p></div>
<div class="item" style="left:80px;top:983px;background:#f0f0f0"><div class="th" role="img" aria-label="Athlete portrait"></div><h5>Lorem ipsum dolor sit .</h5><p>Proin ornare augue purus, eu cursus nibh vestibulum quis.</p></div>

<div class="abs mid" style="left:327px;top:824px">
  <h3>SPORT STATS ON DEMAND</h3>
  <p>Forget about relying on sportcasters or the banner moving on the bottom of your screen for the scores you want. Just select your league, go to team data, go to the game you're interested in and get the score. All in a matter of seconds.</p>
</div>
<div class="abs sponsors">
  <div class="cond" style="font-size:15.5px;color:var(--navy)">OUR SPONSORS</div>
  <span class="dots">●●●●●●●</span>
  <div class="badges">
    <span style="background:#1e3a7a"></span><span style="background:#d8b04a"></span><span style="background:#2a7ad0"></span><span style="background:#c8303a"></span><span style="background:#d83a30"></span>
  </div>
</div>

<div class="abs tabhead" style="left:574px;top:820px;width:212px;background:var(--navy);color:#fff">PAST TEAM PERFORMANCE</div>
<div class="item blue" style="left:574px;top:853px;background:#f0f0f0"><div class="th" role="img" aria-label="Athlete portrait"></div><h5>Milford</h5><p>Lorem ispum plase ispum Proin ornare augue lorempu</p></div>
<div class="item alt" style="left:574px;top:918px"><div class="th" role="img" aria-label="Athlete portrait"></div><h5>Lorem ipsum dolor sit .</h5><p>Proin ornare augue purus, eu cursus nibh vestibulum quis.</p></div>
<div class="item" style="left:574px;top:983px;background:#f0f0f0"><div class="th" role="img" aria-label="Footballer portrait"></div><h5>Lorem ipsum dolor sit .</h5><p>Proin ornare augue purus, eu cursus nibh vestibulum quis.</p></div>

<footer class="abs footer">
  <h3 style="left:80px;top:14px">RUNLARK MOBILE APPS ARE HERE</h3>
  <div class="abs store" style="left:80px"><i></i>Available on the<b>App Market</b></div>
  <div class="abs store" style="left:225px"><i></i>Get it on<b>Play Shelf</b></div>
  <h3 style="left:518px;top:14px">SUBSCRIBE WITH US:</h3>
  <div class="abs email">Enter your Email...</div>
  <svg class="abs" style="left:524px;top:48px" width="34" height="20" viewBox="0 0 34 20"><rect x="1" y="1" width="32" height="18" fill="none" stroke="#555" stroke-width="1.5"/><path d="M1 1l16 10L33 1M1 19l12-9M33 19l-12-9" fill="none" stroke="#555" stroke-width="1.5"/></svg>
  <div class="abs send"><svg width="29" height="28" viewBox="0 0 29 28"><path d="M9 7l13 7-13 7 2-7z" fill="#fff"/></svg></div>
</footer>

<div class="abs bottombar">
  <div class="links"><a href="#">Home</a> &nbsp;/&nbsp; About Us &nbsp;/&nbsp; Events &nbsp;/&nbsp; Live Scores &nbsp;/&nbsp; News &nbsp;/&nbsp; Sports &nbsp;/&nbsp; Photos &nbsp;/&nbsp; Faqs &nbsp;/&nbsp; Contact Us</div>
  <div class="copy">© 2014 Runlark. All right reserved</div>
</div>

</body>
</html>
```